Varnecke Holdings Webpage Design

We need a new website for our company. The company is Varnecke Holdings Pty Ltd. We are in the business of Asbestos Removal; Demolition; Earthworks and Transport. We do not advertise and would like our website to be a reference point for our clients / potential clients and also to make our services known to those searching the internet for the services we offer. Some examples of the style of website we are after are:
http://www.quillmarkwrecking.example.au/
http://m.tovrinbrookclearing.example.au/
http://www.pellowayclearance.example.au
http://www.zorvat.example.au
http://www.kjbworks.example.au
http://www.northpeak-dismantling.example.au
We will need to work on content. Enclosed is an example. We also need to purchase the domain varneckeholdings.example.au and need to set up email accounts and ensure the website is mobile friendly. We have a company logo and have built our business on delivering professional, quality services on time. We would like the webpage to be simple, informative and professional - black and white / grey themed. We would also like to add a photo gallery etc later.

Colors
000000
fcfcfc
959595
dddddd

Requirements
Must have
• Information regarding the services we provide

```html
<!DOCTYPE html>
<html lang="en">
<head>
<meta charset="utf-8">
<title>Varnecke Holdings</title>
<link rel="stylesheet" href="https://fonts.googleapis.com/css2?family=Michroma&family=Jura:wght@400;500&family=Open+Sans:wght@400;700&family=Roboto+Condensed:wght@400&display=swap">
<style>
  :root {
    --ink: #000000;
    --bar: #231f20;
    --paper: #fcfcfc;
    --white: #ffffff;
    --mid: #959595;
    --light: #dddddd;
    --text: #222222;
    --muted: #666666;
  }
  * { box-sizing: border-box; margin: 0; padding: 0; }
  html, body { width: 1200px; height: 2568px; overflow: hidden; }
  body { background: var(--white); font-family: 'Open Sans', sans-serif; color: var(--text); }
  .page { position: relative; width: 1200px; height: 2568px; }

  .site-header { height: 104px; background: var(--bar); display: flex; align-items: center; padding: 0 77px; justify-content: space-between; }
  .brand { display: flex; align-items: center; gap: 14px; width: 368px; color: var(--white); font-family: 'Jura', sans-serif; font-weight: 500; font-size: 28px; letter-spacing: 1px; white-space: nowrap; }
  .brand-mark { width: 22px; height: 22px; background: var(--white); flex: none; }
  .main-nav { display: flex; gap: 8px; margin-right: -8px; }
  .main-nav a { font-family: 'Roboto Condensed', sans-serif; color: #d8d8d8; text-decoration: none; font-size: 19px; padding: 10px 14px; }
  .main-nav a.active { background: var(--ink); color: var(--white); }

  .hero { position: relative; height: 589px; background: linear-gradient(180deg, #4f6c86 0%, #9fb3c3 30%, #d9dcdc 48%, #a89888 62%, #bcb5ad 78%, #e8e6e4 100%); }
  .hero-tagline { position: absolute; left: 0; right: 0; top: 458px; text-align: center; font-family: 'Jura', sans-serif; font-weight: 500; font-size: 40px; line-height: 54px; color: var(--bar); letter-spacing: 1px; }

  .welcome { height: 315px; text-align: center; padding-top: 54px; }
  .section-title { font-family: 'Jura', sans-serif; font-weight: 500; font-size: 40px; color: var(--ink); line-height: 1.2; }
  .section-title strong { font-family: 'Michroma', sans-serif; font-weight: 400; font-size: 34px; }
  .welcome p { width: 840px; margin: 22px auto 0; font-size: 15.5px; line-height: 25px; }
  .btn { display: inline-block; background: var(--bar); color: var(--white); font-family: 'Jura', sans-serif; font-weight: 500; font-size: 22px; padding: 0 24px; height: 46px; line-height: 46px; border-radius: 3px; text-decoration: none; }
  .welcome .btn { margin-top: 24px; width: 173px; }

  .services { height: 516px; background: linear-gradient(180deg, #c4c4c4, #dcdcdc 60%, #cfcfcf); text-align: center; padding-top: 62px; }
  .service-cards { display: flex; gap: 36px; margin: 30px 0 0 77px; }
  .service-card { width: 235px; height: 311px; background: var(--white); }
  .service-photo { height: 135px; }
  .service-card h3 { font-weight: 400; font-size: 23px; color: var(--ink); margin-top: 20px; }
  .service-card p { font-size: 15px; line-height: 25px; color: var(--muted); padding: 6px 10px 0; }

  .testimonials { height: 470px; text-align: center; padding-top: 52px; }
  .testimonials .section-title { color: var(--mid); }
  .testimonials .section-title span { color: var(--ink); }
  .quote-box { position: relative; width: 885px; height: 153px; margin: 50px auto 0; background: var(--light); border-radius: 4px; padding: 22px 60px; font-size: 15.5px; line-height: 25px; }
  .quote-box::after { content: ""; position: absolute; left: 50%; bottom: -12px; margin-left: -12px; border: 12px solid transparent; border-bottom: 0; border-top-color: var(--light); }
  .client-name { font-size: 21px; margin-top: 6px; }
  .slider-arrows { display: flex; justify-content: center; gap: 25px; margin-top: 8px; }
  .slider-arrows span { width: 57px; height: 57px; border: 2px solid var(--bar); border-radius: 50%; display: flex; align-items: center; justify-content: center; }

  .cta { height: 292px; background: linear-gradient(180deg, #e4e4e4, #bdbdbd 55%, #d4d4d4); text-align: center; padding-top: 70px; }
  .cta p { font-size: 22px; line-height: 31px; color: var(--ink); }
  .cta .btn { margin-top: 27px; width: 184px; }

  .site-footer { height: 282px; background: var(--bar); color: var(--white); padding: 0 77px; }
  .footer-top { height: 107px; display: flex; align-items: center; justify-content: space-between; border-bottom: 1px solid #3d393a; }
  .footer-nav { display: flex; gap: 38px; }
  .footer-nav a { color: var(--white); text-decoration: none; font-size: 18px; }
  .social { display: flex; gap: 22px; }
  .social span { width: 51px; height: 51px; border: 2px solid var(--white); border-radius: 50%; }
  .social span.first { background: var(--white); }
  .footer-contact { display: flex; height: 88px; align-items: center; }
  .contact-item { display: flex; align-items: center; gap: 14px; font-size: 16px; line-height: 25px; }
  .contact-item .icon { width: 53px; height: 53px; border: 2px solid var(--white); border-radius: 50%; display: flex; align-items: center; justify-content: center; flex: none; }
  .contact-item.address { width: 442px; }
  .contact-item.phone { width: 293px; }
  .copyright { text-align: center; font-size: 15px; color: var(--mid); margin-top: 14px; }
  .copyright strong { color: var(--white); }
</style>
</head>
<body>
<div class="page">
  <header class="site-header">
    <div class="brand"><span class="brand-mark"></span><span>VARNECKE HOLDINGS</span></div>
    <nav class="main-nav">
      <a class="active" href="#">HOME</a><a href="#">ABOUT</a><a href="#">SERVICES</a><a href="#">SAFETY</a><a href="#">ENVIRONMENT</a><a href="#">CONTACT</a>
    </nav>
  </header>

  <section class="hero" role="img" aria-label="Yellow bulldozer and dump truck on a quarry site under a cloudy sky">
    <div class="hero-tagline">TRANSPORT &bull; DEMOLITION &bull; EARTHMOVING</div>
  </section>

  <section class="welcome">
    <h1 class="section-title">WELCOME TO <strong>VARNECKE HOLDINGS</strong></h1>
    <p>Varnecke Transport Pty Ltd was established by Director Martin Varnecke in 2002 with a focus providing services within the transport industry. Over time the company has developed and expanded to include the provision of Earthworks and Demolition.</p>
    <a class="btn" href="#">READ MORE</a>
  </section>

  <section class="services">
    <h2 class="section-title">OUR SERVICES</h2>
    <div class="service-cards">
      <article class="service-card">
        <div class="service-photo" role="img" aria-label="Excavator breaking up concrete on a demolition site" style="background:linear-gradient(180deg,#6a9fd0,#b9a27a 60%,#7d6b55)"></div>
        <h3>Demolition</h3>
        <p>Varnecke Transport and Demolition provide an extensive range of demolition services.</p>
      </article>
      <article class="service-card">
        <div class="service-photo" role="img" aria-label="Wheel loader moving earth and rock" style="background:linear-gradient(180deg,#8aa3b8,#6d6250 55%,#4a4238)"></div>
        <h3>Earthworks</h3>
        <p>Varnecke Transport and Demolition possess all necessary equipment and skilled personnel...</p>
      </article>
      <article class="service-card">
        <div class="service-photo" role="img" aria-label="Corrugated asbestos cement roof sheeting" style="background:linear-gradient(180deg,#6e8f5a,#b8b8b3 45%,#8f8f8a)"></div>
        <h3>Asbestos</h3>
        <p>Asbestos is a naturally occurring silicate mineral made up of tiny fibres.</p>
      </article>
      <article class="service-card">
        <div class="service-photo" role="img" aria-label="Yellow excavator digging sand under a blue sky" style="background:linear-gradient(180deg,#3f7dc4,#a9c4e0 45%,#c8a46a)"></div>
        <h3>Hours of Operation</h3>
        <p>Varnecke Transport and Demolition operate Monday to Saturday.</p>
      </article>
    </div>
  </section>

  <section class="testimonials">
    <h2 class="section-title">WHAT OUR <span>CLIENT SAY</span></h2>
    <blockquote class="quote-box">Lorem Ipsum is simply dummy text of the printing and typesetting industry. Lorem Ipsum has been the industry's standard dummy text ever since the 1500s, when an unknown printer took a galley of type and scrambled it to make a type specimen book.</blockquote>
    <div class="client-name">- Client Name</div>
    <div class="slider-arrows">
      <span><svg width="22" height="28" viewBox="0 0 22 28"><path d="M16 3 L6 14 L16 25" fill="none" stroke="#231f20" stroke-width="5"/></svg></span>
      <span><svg width="22" height="28" viewBox="0 0 22 28"><path d="M6 3 L16 14 L6 25" fill="none" stroke="#231f20" stroke-width="5"/></svg></span>
    </div>
  </section>

  <section class="cta" role="img" aria-label="Faded greyscale photo of a wheel loader on a work site">
    <p>Lorem Ipsum is simply dummy text of the printing and typesetting industry.<br>Lorem Ipsum has been the industry's standard dummy text.</p>
    <a class="btn" href="#">GET QUOTE</a>
  </section>

  <footer class="site-footer">
    <div class="footer-top">
      <nav class="footer-nav"><a href="#">Home</a><a href="#">About</a><a href="#">Services</a><a href="#">Safety</a><a href="#">Environment</a><a href="#">Contact</a></nav>
      <div class="social"><span class="first" aria-label="Social link"></span><span aria-label="Social link"></span><span aria-label="Social link"></span></div>
    </div>
    <div class="footer-contact">
      <div class="contact-item address">
        <span class="icon"><svg width="20" height="26" viewBox="0 0 20 26"><path d="M10 1 C4.5 1 1 5 1 9.5 C1 16 10 25 10 25 C10 25 19 16 19 9.5 C19 5 15.5 1 10 1 Z" fill="#fff"/><circle cx="10" cy="9.5" r="3.5" fill="#231f20"/></svg></span>
        <span>PO Box 512 KELVALE<br>QLD 4391</span>
      </div>
      <div class="contact-item phone">
        <span class="icon"><svg width="24" height="24" viewBox="0 0 24 24"><path d="M6 2 L10 7 L7.5 10 C9 13 11 15 14 16.5 L17 14 L22 18 L19 22 C11 21 3 13 2 5 Z" fill="#fff"/></svg></span>
        <span>0400 000 117<br>0400 000 482</span>
      </div>
      <div class="contact-item email">
        <span class="icon"><svg width="24" height="18" viewBox="0 0 24 18"><rect x="1.5" y="1.5" width="21" height="15" rx="2" fill="none" stroke="#fff" stroke-width="2"/><path d="M2 3 L12 10 L22 3" fill="none" stroke="#fff" stroke-width="2"/></svg></span>
        <span>office@varneckeholdings.example.au</span>
      </div>
    </div>
    <div class="copyright">&copy; <strong>VARNECKE HOLDINGS</strong> - 2015. All Rights Reserved.</div>
  </footer>
</div>
</body>
</html>
```